eCommerce website home page design for Verantis Blue Hydrofarms
Verantis Blue Hydrofarms
eCommerce website home page design for Verantis Blue Hydrofarms - Miscellaneous
Creative Brief
Miscellaneous
www.vbhydrofarms-example.com
In Aquaponics fish and vegetables are grown together. Our home aquaponic systems are aimed at people who what healthy toxin free fish and vegetables grown in an environmentally sustainable way. This will be an eCommerce website. We are looking for a design that has a polished / professional look but is not so flashy that it gets in the way ofthe buying experience
see above
Nature
colors should match those in the logo
use additional color of your choice
I'm OK with white spaces if you think they work
left side
http://www.plovamerch-example.com.au/
http://www.kelbrino-example.de/
http://www.rolp-quik-example.com/
The uploaded rough layout shows some of the elements we want to highlight. You can completely re-do the design or polish the layout that I have roughed out. There does not need to be both a top and left navigation menu. There can be either or both. I have uploaded the logo and images from the rough layout. You can use these or different images, whatever you think
vbhydrofarms vbhydrofarms
with Aquaponics there does need to be a certain amount of education, since most people have not heard about it. I am thinking we want the three categories of "What is Aquaponics","Why Aquaponics" and "Aquaponics Systems"on the home page. Although you can change the layout from the rough design I have uploaded.
Please keep in mind we sell aquaponic systems. If you need more information there is some at our website www.vbhydrofarms-example.com under systems or learn aquaponics. Also you can do a search under aquaponics. We do not sell fish or vegetables

```html
<!DOCTYPE html>
<html lang="en">
<head>
<meta charset="utf-8">
<title>Verantis Blue Hydrofarms — Home</title>
<link href="https://fonts.googleapis.com/css2?family=Ubuntu:wght@400;500;700&family=Arimo:wght@400;700&display=swap" rel="stylesheet">
<style>
:root{
  --night:#05183a;
  --sky:#3d9fd6;
  --brand-blue:#0f5fb8;
  --nav-blue:#0c62c4;
  --nav-blue-dark:#0a4fa6;
  --leaf:#5e8b12;
  --leaf-light:#8cc63f;
  --deep-green:#3f7a25;
  --footer-dark:#1c3a86;
  --footer-mid:#2579c0;
  --text:#505050;
  --link:#0d4f9c;
  --white:#ffffff;
}
*{box-sizing:border-box;margin:0;padding:0}
html,body{width:1186px;height:1200px;overflow:hidden}
body{
  background:linear-gradient(180deg,var(--night) 0%,#0f3d78 35%,#2f86c6 75%,var(--sky) 100%);
  font-family:"Arimo",Arial,sans-serif;color:var(--text);position:relative;
}
.page{position:absolute;left:151px;top:30px;width:887px;height:1138px;background:var(--white);border-top:4px solid var(--leaf-light);overflow:hidden}
.abs{position:absolute}

/* header */
.brand{left:28px;top:27px;display:flex;align-items:center;gap:12px}
.brand-dot{width:66px;height:66px;border-radius:50%;background:var(--brand-blue)}
.brand-name{font-family:"Ubuntu",sans-serif;font-weight:700;color:var(--brand-blue);line-height:1.05}
.brand-name .l1{display:block;font-size:29px;letter-spacing:.5px}
.brand-name .l2{display:block;font-size:20px;letter-spacing:6px}
.toplinks{right:30px;top:36px;display:flex;align-items:center;font-size:9px;color:var(--link)}
.toplinks a{color:var(--link);text-decoration:none}
.toplinks .sep{margin:0 8px;color:#333}
.toplinks .cart{display:flex;align-items:center;gap:4px;margin-left:6px;color:#333;font-weight:700}
.search{left:552px;top:67px;width:305px;height:28px;border:1px solid #dcdcdc;background:#f7f7f7;display:flex}
.search span{flex:1;font-size:9px;color:#8a8a8a;padding:9px 0 0 12px}
.search i{width:28px;border-left:1px solid #dcdcdc;display:flex;align-items:center;justify-content:center}

/* nav */
.nav{left:30px;top:118px;width:827px;height:37px;background:linear-gradient(180deg,var(--nav-blue),var(--nav-blue-dark));display:flex;justify-content:space-between;padding:0 8px}
.nav a{color:var(--white);font-size:10.3px;font-weight:700;text-decoration:none;display:flex;align-items:center;padding:0 22px;border-right:1px solid rgba(255,255,255,.15)}
.nav a:last-child{border-right:0}

/* hero */
.hero{left:30px;top:155px;width:827px;height:321px;overflow:hidden}
.hero-photo{position:absolute;inset:0;background:
  radial-gradient(ellipse at 25% 40%,#7fb84a 0%,transparent 55%),
  radial-gradient(ellipse at 12% 20%,#7a2a3a 0%,transparent 30%),
  radial-gradient(ellipse at 75% 45%,#4aa890 0%,transparent 60%),
  linear-gradient(90deg,#4d8a2e,#6aaa6a 50%,#3d9a88)}
.hero-arrow{position:absolute;top:104px;width:58px;height:58px;border-radius:50%;background:rgba(255,255,255,.35)}
.hero-arrow.prev{left:-30px}.hero-arrow.next{right:-30px}
.hero-arrow svg{position:absolute;top:19px}
.hero-arrow.prev svg{right:9px}.hero-arrow.next svg{left:9px}
.hero-caption{position:absolute;left:0;right:0;bottom:0;height:66px;background:linear-gradient(90deg,rgba(10,30,15,.72),rgba(10,30,15,.55) 80%,rgba(10,30,15,.2));padding:12px 0 0 13px;color:var(--white)}
.hero-caption h1{font-family:"Ubuntu",sans-serif;font-weight:500;font-size:20.5px;letter-spacing:.2px}
.hero-caption p{font-size:11.6px;margin-top:5px}
.hero-caption a{color:var(--white);font-style:italic}

/* cards */
.card{top:511px;width:248px}
.card-media{position:relative;height:166px;overflow:hidden}
.card-head{position:absolute;left:0;top:0;right:0;height:37px;display:flex;align-items:center;gap:8px;padding-left:6px;color:var(--white);font-family:"Ubuntu",sans-serif;font-size:18.5px}
.card-head .dot{width:21px;height:21px;border-radius:50%;background:var(--white);opacity:.9}
.head-blue{background:linear-gradient(180deg,#2a7fd0,#0c56ab)}
.head-navy{background:linear-gradient(180deg,#0f3d78,#0a2f62)}
.head-green{background:linear-gradient(180deg,#0c3a1a,#23652a)}
.card-img{position:absolute;left:0;right:0;top:37px;bottom:0}
.img-intro{background:linear-gradient(135deg,#9bd25a 0%,#5fae2e 45%,#1a68b8 60%,#5fb0e8 100%)}
.img-veg{background:linear-gradient(180deg,#6aa23a 0%,#c83a1a 35%,#e0a040 60%,#8a5a28 100%)}
.img-sys{background:linear-gradient(180deg,#f2f2f2,#d8d8d8);}
.img-sys::after{content:"";position:absolute;left:60px;top:6px;width:128px;height:112px;background:linear-gradient(180deg,#c96a7a,#b5566a);opacity:.55}
.play{position:absolute;right:5px;bottom:5px;font-size:7px;font-weight:700;color:rgba(255,255,255,.85)}
.card p{font-size:11.6px;line-height:17.3px;margin-top:19px;color:var(--text)}
.card p em{font-style:normal;color:var(--deep-green)}
.btn{position:absolute;height:26px;background:var(--leaf);color:var(--white);font-size:12.5px;display:flex;align-items:center;justify-content:center;border-radius:1px}

/* footer */
.footer-art{left:0;top:798px;width:887px;height:340px}
.f-col{top:967px;color:var(--white)}
.f-col h3{font-size:14px;font-weight:700;margin-bottom:9px}
.f-col ul{list-style:none}
.f-col li{font-size:10.7px;height:19.6px;position:relative;padding-left:14px}
.f-col li::before{content:"";position:absolute;left:1px;top:2px;border-left:5px solid var(--white);border-top:4px solid transparent;border-bottom:4px solid transparent}
.f-contact p{font-size:10.7px;line-height:13px}
.f-contact .row{display:flex;align-items:center;gap:4px;font-size:10.7px;height:18px}
.field{width:195px;height:27px;background:var(--white);border:1px solid #c8d4e4;font-size:10px;color:#333;display:flex;align-items:center;justify-content:space-between;padding:0 9px 0 6px}
.subscribe{width:64px;height:27px;background:linear-gradient(180deg,#8cc63f,#5e9a17);color:var(--white);font-size:10px;font-weight:700;display:flex;align-items:center;justify-content:center;margin:11px 0 0 131px}
.bottom-bar{left:0;top:1100px;width:887px;height:38px;background:rgba(20,50,120,.35);border-top:1px solid rgba(255,255,255,.12);color:var(--white);font-size:9px;display:flex;align-items:center;justify-content:space-between;padding:0 30px 0 31px}
.follow{display:flex;align-items:center;gap:13px;font-weight:700}
.social{width:18px;height:18px;border-radius:3px;background:#d7e3f1}
</style>
</head>
<body>
<div class="page">

  <header>
    <div class="abs brand">
      <span class="brand-dot"></span>
      <span class="brand-name"><span class="l1">VERANTIS BLUE</span><span class="l2">HYDROFARMS</span></span>
    </div>
    <nav class="abs toplinks">
      <a href="#">Online Store</a><span class="sep">|</span>
      <a href="#">Books &amp; Videos</a><span class="sep">|</span>
      <a href="#">Learn Aquaponics</a><span class="sep">|</span>
      <a href="#">Register Now</a><span class="sep">|</span>
      <a href="#">My Account</a>
      <span class="cart"><svg width="18" height="15" viewBox="0 0 18 15"><path d="M1 2h3l2 8h9l2-6H5" fill="none" stroke="#777" stroke-width="1.2"/><circle cx="7" cy="13" r="1.3" fill="#777"/><circle cx="14" cy="13" r="1.3" fill="#777"/></svg>My Cart</span>
    </nav>
    <div class="abs search"><span>Type your search</span><i><svg width="12" height="12" viewBox="0 0 12 12"><circle cx="7" cy="5" r="3.5" fill="none" stroke="#666" stroke-width="1.2"/><path d="M4.5 7.5 1 11" stroke="#666" stroke-width="1.4"/></svg></i></div>
  </header>

  <nav class="abs nav">
    <a href="#">HOME</a><a href="#">ABOUT US</a><a href="#">SYSTEMS</a><a href="#">REFERRAL PROGRAM</a><a href="#">DISTRIBUTOR</a><a href="#">WHERE TO BUY</a><a href="#">CONTACT US</a>
  </nav>

  <section class="abs hero">
    <div class="hero-photo" role="img" aria-label="Photo of leafy lettuce beside fish swimming in clear green water"></div>
    <span class="hero-arrow prev"><svg width="12" height="22" viewBox="0 0 12 22"><path d="M11 1 1 11l10 10" fill="none" stroke="#333" stroke-width="1.2"/></svg></span>
    <span class="hero-arrow next"><svg width="12" height="22" viewBox="0 0 12 22"><path d="M1 1l10 10L1 21" fill="none" stroke="#333" stroke-width="1.2"/></svg></span>
    <div class="hero-caption">
      <h1>FISH AND VEGETABLES ARE GROWN TOGETHER</h1>
      <p>Aquaponics, Low Cost of Operation &amp; Small Amount of Water Innovative Modular Systems and Sophisticated Marketing Material <a href="#">read more...</a></p>
    </div>
  </section>

  <article class="abs card" style="left:30px">
    <div class="card-media">
      <div class="card-img img-intro" role="img" aria-label="Blue and green leaf graphic introducing an aquaponics video"></div>
      <div class="card-head head-navy"><span class="dot"></span>What is Aquaponics</div>
      <span class="play">PLAY VIDEO ▸</span>
    </div>
    <p>Lorem Ipsum is simply dummy text of the printing and typesetting industry. Lorem Ipsum has been the industry's standard dummy text ever since</p>
  </article>
  <article class="abs card" style="left:318px">
    <div class="card-media">
      <div class="card-img img-veg" role="img" aria-label="Basket of fresh vegetables: tomatoes, peppers, onions, garlic and greens"></div>
      <div class="card-head head-green"><span class="dot"></span>Why Aquaponics</div>
    </div>
    <p>Lorem Ipsum is simply dummy text of the printing and typesetting industry. Lorem Ipsum has been the industry's standard dummy text ever since</p>
  </article>
  <article class="abs card" style="left:609px">
    <div class="card-media">
      <div class="card-img img-sys" role="img" aria-label="Two-tier home aquaponics unit with plant bed above fish tank"></div>
      <div class="card-head head-blue"><span class="dot"></span>Aquaponics Systems</div>
    </div>
    <p>Lorem Ipsum is simply dummy text of the printing and typesetting industry. Lorem Ipsum has been <em>Books/Video</em> standard dummy text ever since</p>
  </article>

  <a class="btn" style="left:197px;top:767px;width:84px">Read More</a>
  <a class="btn" style="left:484px;top:767px;width:84px">Read More</a>
  <a class="btn" style="left:766px;top:767px;width:89px">Read More</a>

  <svg class="abs footer-art" viewBox="0 0 887 340" preserveAspectRatio="none" aria-hidden="true">
    <defs>
      <linearGradient id="footBlue" x1="0" y1="0" x2="1" y2="0.4">
        <stop offset="0" stop-color="#1c3a86"/><stop offset=".55" stop-color="#2579c0"/><stop offset="1" stop-color="#1d4b98"/>
      </linearGradient>
      <linearGradient id="leafBand" x1="0" y1="0" x2="1" y2="0">
        <stop offset="0" stop-color="#3f7a25"/><stop offset=".5" stop-color="#8cc63f"/><stop offset="1" stop-color="#4d8f2a"/>
      </linearGradient>
    </defs>
    <path d="M0 40 C180 150 480 175 887 60 L887 340 L0 340Z" fill="url(#footBlue)"/>
    <path d="M0 0 C60 110 340 160 887 54 L887 60 C420 165 170 150 0 58Z" fill="url(#leafBand)"/>
    <path d="M0 96 C200 160 470 175 887 66" fill="none" stroke="#ffffff" stroke-width="1.6"/>
    <path d="M0 60 C220 150 520 170 887 62" fill="none" stroke="#3aa0e0" stroke-width="1.2" opacity=".7"/>
  </svg>

  <div class="abs f-col" style="left:31px">
    <h3>Quick Links</h3>
    <ul><li>Home Page</li><li>About us</li><li>Prodcts</li><li>Where to Buy</li><li>Contact Us</li></ul>
  </div>
  <div class="abs f-col" style="left:231px">
    <h3>More About Us</h3>
    <ul><li>My Account</li><li>Register With Us</li><li>Feedback</li><li>Testimonials</li><li>Books and Videos</li></ul>
  </div>
  <div class="abs f-col f-contact" style="left:438px">
    <h3>Contact Us</h3>
    <p>4810 Larkmoor Lane, Unit C<br>Fernvale, Ohio 45011</p>
    <div class="row" style="margin-top:4px"><svg width="8" height="9" viewBox="0 0 8 9"><path d="M2 0 0 2c0 4 3 7 6 7l2-2-2-2-1 1C4 6 3 5 2 4l1-1z" fill="#fff"/></svg>866 555 0143 (voice/fax)</div>
    <div class="row"><svg width="6" height="9" viewBox="0 0 6 9"><rect x=".5" y=".5" width="5" height="8" rx="1" fill="none" stroke="#fff"/></svg>248 555 0187 (direct)</div>
    <div class="row"><svg width="8" height="6" viewBox="0 0 8 6"><rect width="8" height="6" fill="#fff"/><path d="M0 0l4 3 4-3" fill="none" stroke="#2579c0"/></svg>hello@vbhydrofarms-example.com</div>
  </div>
  <div class="abs f-col" style="left:662px;top:961px">
    <h3 style="margin-bottom:12px">Get Our Latest Updates</h3>
    <div class="field">Enter Your Name<svg width="12" height="12" viewBox="0 0 12 12"><circle cx="6" cy="3.5" r="3" fill="#555"/><path d="M0 12c0-4 3-5 6-5s6 1 6 5z" fill="#555"/></svg></div>
    <div class="field" style="margin-top:9px">Enter Your Email<svg width="13" height="9" viewBox="0 0 13 9"><rect x=".5" y=".5" width="12" height="8" fill="none" stroke="#555"/><path d="M.5.5 6.5 5l6-4.5" fill="none" stroke="#555"/></svg></div>
    <div class="subscribe">Subscribe</div>
  </div>

  <footer class="abs bottom-bar">
    <span>Copyright © 2010-2013 &nbsp;www.vbhydrofarms-example.com &nbsp;All Rights Reserved &nbsp; Privacy &nbsp;| &nbsp;Terms</span>
    <span class="follow">Follow Us <i class="social"></i><i class="social"></i><i class="social"></i><i class="social"></i><i class="social"></i></span>
  </footer>

</div>
</body>
</html>
```